Tinker's Fox sports bar beer & food menu

We need a menu design for our gastropub sports bar in L.A.'s Sawtelle Neighborhood (Little Osaka). We have a full-bar (hard liquor, craft beer, wine and cocktails) . We have a lunch and dinner menu as well as a happy hour menu. On Sundays we have a seperate menu with brunch items. The design concept is a British pub type of sports bar. We're looking for something different from our existing menu design. Ideally something cleaner and more legible. It should mesh a simple, modern sensibility with the more traditional darkened pub style of our interior design.

You can check out our Venuvista page for photos of the interior/exterior:
https://www.venuvista.com/biz_photos/tinkers-fox-los-angeles?tab=interior

You can view our existing menu here:
https://www.venuvista.com/biz_photos/tinkers-fox-los-angeles?tab=menu

If there's an area of the design that can be a little more playful it's our highlighted event schedule so that the events will stand out.

Target Market(s)

Age of 25 and up. Sawtelle is a cultural hub that caters to a younger, moderately affluent crowd.

Industry/Entity Type

Sports Bar

Font styles to use
Sans Serif

Colors

Designer to choose colors to be used in the design.

Requirements
Must have
• Logo, highlighted event schedule (beer pong Monday, trivia Tuesday, taco Tuesday, whiskey Wednesday, karaoke Saturday). The menu should be easy to read in a darkened bar. We'll be printing on standard 8.5x11 in portrait.
Nice to have
• We're trying to have the menu take up as few pages as possible.
Should not have
• We're trying to have the menu take up as few pages as possible. Food photography isn't necessary. A cover isn't necessary. Please avoid clip art of food.

```html
<!DOCTYPE html>
<html lang="en">
<head>
<meta charset="utf-8">
<title>Tinker's Fox Pub &amp; Restaurant – Menu Pages 03–04</title>
<link rel="stylesheet" href="https://fonts.googleapis.com/css2?family=Cabin:wght@500;600;700&display=swap">
<style>
  :root {
    --backdrop: #d3dcdb;
    --page: #2f3133;
    --band-edge: #f5a000;
    --band-mid: #ffc51f;
    --ink-dark: #1d1d1d;
    --accent: #f7a21b;
    --text: #ffffff;
    --label-bg: #ffffff;
    --tab: #3b3e41;
  }
  * { box-sizing: border-box; margin: 0; padding: 0; }
  html, body {
    width: 1200px; height: 942px; overflow: hidden;
    background: var(--backdrop);
    font-family: "Cabin", sans-serif;
  }
  .spread {
    position: absolute; left: 30px; top: 43px;
    width: 1140px; height: 856px;
    display: flex;
  }
  .page {
    position: relative; width: 570px; height: 856px;
    background: var(--page); overflow: hidden;
  }
  .page + .page { border-left: 1px solid #26282a; }
  .brand-band {
    position: absolute; left: 0; right: 0; top: 58px; height: 124px;
    background: linear-gradient(90deg, var(--band-edge), var(--band-mid) 50%, var(--band-edge));
    display: flex; align-items: center; justify-content: center; gap: 14px;
  }
  .brand-mark {
    width: 38px; height: 38px; border-radius: 50%;
    background: var(--ink-dark);
  }
  .brand-text { display: flex; flex-direction: column; align-items: center; }
  .brand-name {
    font-weight: 700; font-size: 50px; line-height: 1; color: var(--ink-dark);
  }
  .brand-tagline {
    margin-top: 6px; font-weight: 700; font-size: 11px;
    letter-spacing: 5px; color: var(--ink-dark);
  }
  .column {
    position: absolute; top: 236px; width: 262px;
    text-align: center; color: var(--text);
    font-weight: 600; font-size: 11.2px; line-height: 18.7px;
  }
  .item { color: var(--accent); }
  .section-label {
    display: inline-block; background: var(--label-bg); color: var(--accent);
    font-weight: 700; font-size: 17px; line-height: 28px; padding: 0 12px;
    box-shadow: 2px 4px 5px rgba(0,0,0,.45);
    margin-bottom: 14px;
  }
  .section-label.wide { padding: 0 10px; }
  .section-gap { margin-top: 10px; }
  .sides-row { display: flex; justify-content: center; gap: 26px; }
  .divider {
    position: absolute; width: 2px; background: var(--accent);
  }
  .divider::before, .divider::after {
    content: ""; position: absolute; left: -3px; width: 8px; height: 8px;
    border-radius: 50%; background: var(--accent);
  }
  .divider::before { top: -4px; }
  .divider::after { bottom: -4px; }
  .page-number {
    position: absolute; right: 0; width: 56px; height: 28px;
    background: var(--tab); color: var(--text);
    font-weight: 700; font-size: 15px; line-height: 28px;
    text-align: center; padding-left: 8px;
    clip-path: polygon(14px 0, 100% 0, 100% 100%, 14px 100%, 0 50%);
  }
</style>
</head>
<body>
<main class="spread">

  <section class="page page-left">
    <header class="brand-band">
      <span class="brand-mark"></span>
      <div class="brand-text">
        <span class="brand-name">Tinker's Fox</span>
        <span class="brand-tagline">PUB &amp; RESTAURANT</span>
      </div>
    </header>

    <div class="column" style="left:18px;">
      <div class="section-label">For the Table</div>
      <div class="item">Tinker's 3 Whole Wings $9</div>
      <div>Choice of Dry Rub, Sweet N' Spicy or Buffalo</div>
      <div class="item">Brussel Sprouts $8</div>
      <div>Sautéed with Chorizo, Roasted Almonds and Golden Raisins</div>
      <div class="item">Golden Calamari $11</div>
      <div>Traditionally Served with Spiced Marinara</div>
      <div class="item">Shrimp Mac N' Cheese $12</div>
      <div>Baked with Fontina, Sharp Cheddar and Parmesan</div>
      <div class="item">½ Dozen Oysters $12</div>
      <div>Pebble Cove's Served with Our Own Mignonette</div>
      <div class="item">Charcuterie $15</div>
      <div>Seasonal Meats and Cheese</div>
      <div class="item">Nachos $9</div>
      <div>Medley of Black Beans, Pico De Gallo, Cheese, Jalapeno and Sour Cream</div>
      <div class="item">Mozzarella Cheese Stick $9</div>

      <div class="section-label section-gap">Sides</div>
      <div class="sides-row item"><span>House Fries $6</span><span>Dry Rub Fries $6</span></div>
      <div class="sides-row item"><span>Truffle Fries $7</span><span>Sweet Potato Fries $6</span></div>

      <div class="section-label section-gap">Deserts</div>
      <div class="item">Coco Flan $9/ cheese cake $9/</div>
      <div class="item">Peach tart $9</div>
    </div>

    <div class="divider" style="left:289px; top:318px; height:388px;"></div>

    <div class="column" style="left:296px; width:256px;">
      <div class="section-label">Salads and Soups</div>
      <div class="item">Chili Soupe - Cup $7 Bowl $9</div>
      <div>Turkey with Vegetables, Onions and Sharp Cheddar</div>
      <div class="item">Soup of the day - Cup $5 Bowl $7</div>
      <div class="item">Caesar $10</div>
      <div>Romaine Hearts, Croutons and Shaved Parmesan</div>
      <div class="item">Tinker's Fox Chopped Salad $11</div>
      <div>Romaine, Salami, Provolone, Banana Peppers, Red Onions, Olives, Garbanzos Tomatoes, Celery, Tosses in a Red Wine Vinaigrette</div>
      <div class="item">Southwest Salad $12</div>
      <div>Romaine, Tomato, Corn, Avocado, Tossed with a Jalapeno Cilantro Vinaigrette Garnished with Tortilla Chips, Cheddar and Sour Cream</div>
      <div class="item">Quinoa Salad $12</div>
      <div>Roasted Beets, Asparagus, Brussel Sprouts, Mushrooms, Kale, Watermelon Radish Tossed in a Citrus Vinaigrette</div>
      <div class="item">Add Ons: Chicken $4/</div>
      <div class="item">Shrimp $6/</div>
      <div class="item">Salmon $6/</div>
      <div class="item">Steak $9</div>
    </div>

    <div class="page-number" style="top:800px;">03</div>
  </section>

  <section class="page page-right">
    <header class="brand-band">
      <span class="brand-mark"></span>
      <div class="brand-text">
        <span class="brand-name">Tinker's Fox</span>
        <span class="brand-tagline">PUB &amp; RESTAURANT</span>
      </div>
    </header>

    <div class="column" style="left:16px; width:256px;">
      <div class="section-label wide">HAPPY HOUR: 3-7PM Daily</div>
      <div class="item">Shisito Pepper $6</div>
      <div>Ginger Soy Sauce</div>
      <div class="item">3 Jumbo Wings $6</div>
      <div>Choice of Dry Rub, Sweet N' Spicy or Buffalo</div>
      <div class="item">Meatballs $5</div>
      <div>House Marinara Sauce</div>
      <div class="item">Fried Calamari $6</div>
      <div>Marinara Sauce</div>
      <div class="item">Tinker's Fox Nachos $7</div>
      <div>Medley of Black Beans, Pico De Gallo, Cheese, Jalapeno and Sour Cream</div>
      <div class="item">Pan Roasted Brussel Sprouts $7</div>
      <div>Chorizo, Roasted Almonds and Golden Raisins</div>
      <div class="item">Atlantic Cod Fish N' Chips $8</div>
      <div>House Tartar Sauce, Vinegar and Lemon Wedge</div>
      <div class="item">Tacos (3) $8</div>
      <div>Choose Your Protein: Chicken , Beef or Shrimp</div>
      <div class="item">Beef Sliders (3) $10</div>
      <div>Arugula, Tomato, Onion and Sharp Cheddar</div>
      <div class="item">Fried Chicken Sliders (3) $10</div>
      <div>Coleslaw, Lime Sriracha Sauce</div>
      <div class="item">½ Dozen Oysters $10</div>
      <div>Pebble Cove Served with Our Own Mignonette</div>
      <div class="item">PEI Mussels $11</div>
      <div>Tequila Chipotle Sauce with Cherry Tomatoes and Cilantro</div>
    </div>

    <div class="divider" style="left:284px; top:325px; height:390px;"></div>

    <div class="column" style="left:292px; width:264px; top:230px;">
      <div class="item">Charcuterie $13</div>
      <div>Seasonal Meats and Cheese</div>
      <div class="item">Pita Bread $6</div>
      <div>Hummus Sauce, Shredded Chicken and Avocado</div>
      <div class="item">Mushroom Tart $6</div>
      <div>Portobello Creamy Mushroom with Truffle Oil.</div>
      <div class="item">Shrimp Cocktail (6) $8</div>
      <div>House Cocktail Sauce</div>
      <div class="item">Tomato Bruschetta $6</div>
      <div>Sun-Dried Tomato Pesto, Fresh basil and Tomato Balsamic Glaze</div>

      <div class="section-label wide" style="margin-top:26px;">HAPPY HOUR FLATBREADS</div>
      <div class="item">Margherita $6</div>
      <div>Fresh Mozzarella, Roma Tomatoes and Italian Basil</div>
      <div class="item">Vegetarian $7</div>
      <div>Brussel Sprouts, Peppers, Onions, Zucchini, Goat Cheese , Smoked Mozzarella, Topped with a Balsamic Reduction</div>
      <div class="item">Tikka Masala $7</div>
      <div>Tandoori Chicken, Fontina and Raita</div>
      <div class="item">The Primal Fox $7</div>
      <div>Meatballs, Sausage, Chorizo, Mozzarella &amp;Fresn</div>
      <div class="item">Prosciutto &amp; Arugula $7</div>
      <div>Red Onionin, Parmesans, Mozzarella</div>
      <div class="item">Chicken Tikka Masala $7</div>
      <div>Tandoori, Chicken, Fontini and Raita</div>
    </div>

    <div class="page-number" style="top:806px;">04</div>
  </section>

</main>
</body>
</html>
```